Custom Anatomical Healing Abutment Flyer

Need a Flyer (4x6 inch) color printed suffer for orders..
See attachment for what I'm looking for. just need it to look Nice (eye candy)...

- reduce the number of steps to 5 (pictures included)

you can remove the watermark (have approval from him to use this) just need to add "permission from volminest"

- Tag Line: (can change the wording if needed)
Custom Anatomical Healing Abutment
Available in Silicone and 3D printed

Target Market(s)

Letting customers know of new product available.

Font styles to use
Sans Serif

Colors

Designer to choose colors to be used in the design.

Requirements
Must have
• - reduce the number of steps to 5 (pictures included)
• you can remove the watermark (have approval from him to use this) just need to add "permission from volminest"
Nice to have
• - Tag Line: (can change the wording if needed)
• Custom Anatomical Healing Abutment
• Available in Silicone and 3D printed

```html
<!DOCTYPE html>
<html lang="en">
<head>
<meta charset="UTF-8">
<title>Custom Anatomical Healing Abutment Flyer</title>
<link rel="stylesheet" href="https://fonts.googleapis.com/css2?family=Roboto+Condensed:wght@300;400;700&display=swap">
<style>
  :root{
    --sky-top:#08a6e6;
    --sky-mid:#e4f5fc;
    --sky-low:#b9e3f4;
    --ink:#1d2a33;
    --white:#ffffff;
    --teal:#1aa7ad;
    --teal-dark:#137f84;
    --green:#17a04a;
    --orange:#e8782a;
    --yellow:#f5b52a;
    --navy:#244a6a;
    --blue:#1e9fe0;
    --red:#e8304a;
    --maroon:#5a1b26;
    --ring:#6b6b6b;
  }
  html,body{margin:0;padding:0;overflow:hidden;background:#f2f2f2;}
  .flyer{
    position:relative;width:750px;height:1200px;overflow:hidden;
    background:linear-gradient(180deg,var(--sky-top) 0%,var(--sky-mid) 24%,#f4fbfe 40%,var(--sky-low) 100%);
    font-family:"Roboto Condensed",Arial,sans-serif;
  }
  .title-frame{
    position:absolute;left:55px;top:56px;width:640px;height:126px;
    border:2px solid var(--ink);border-top:none;box-sizing:border-box;
  }
  .title-frame::before,.title-frame::after{
    content:"";position:absolute;top:0;width:40px;border-top:2px solid var(--ink);
  }
  .title-frame::before{left:0}
  .title-frame::after{right:0}
  .title{position:absolute;left:0;right:0;top:-26px;text-align:center;margin:0;line-height:1;}
  .title-lead{display:block;color:var(--white);font-weight:700;font-size:58px;letter-spacing:0.5px;line-height:58px;}
  .title-main{display:block;color:var(--ink);font-weight:300;font-size:66px;line-height:66px;margin-top:2px;}
  .process{position:absolute;left:0;top:0;width:750px;height:1200px;}
  .step-no{font-family:"Roboto Condensed",Arial,sans-serif;font-weight:700;font-size:38px;text-anchor:middle;}
  .offer-band{
    position:absolute;left:0;bottom:0;width:750px;height:142px;background:var(--teal);
    text-align:center;color:var(--white);
  }
  .offer-band::before{content:"";position:absolute;left:0;right:0;top:-6px;border-top:2px solid var(--teal-dark);}
  .offer-kicker{margin:20px 0 0;font-size:38px;font-weight:400;line-height:1;}
  .offer-main{margin:8px 0 0;font-size:60px;font-weight:700;line-height:1;text-shadow:2px 2px 0 #0d3b3e;}
</style>
</head>
<body>
<main class="flyer">
  <header class="title-frame">
    <h1 class="title">
      <span class="title-lead">CUSTOM ANATOMICAL</span>
      <span class="title-main">HEALING ABUTMENT</span>
    </h1>
  </header>

  <svg class="process" viewBox="0 0 750 1200" xmlns="http://www.w3.org/2000/svg">
    <defs>
      <polygon id="hex-frame" points="0,-88 76.2,-44 76.2,44 0,88 -76.2,44 -76.2,-44"/>
      <polygon id="hex-photo" points="0,-70 60.6,-35 60.6,35 0,70 -60.6,35 -60.6,-35"/>
      <marker id="head-yellow" markerWidth="4" markerHeight="4" refX="1" refY="2" orient="auto"><path d="M0,0 L4,2 L0,4 Z" fill="var(--yellow)"/></marker>
      <marker id="head-navy" markerWidth="4" markerHeight="4" refX="1" refY="2" orient="auto"><path d="M0,0 L4,2 L0,4 Z" fill="var(--navy)"/></marker>
      <marker id="head-blue" markerWidth="4" markerHeight="4" refX="1" refY="2" orient="auto"><path d="M0,0 L4,2 L0,4 Z" fill="var(--blue)"/></marker>
      <marker id="head-red" markerWidth="4" markerHeight="4" refX="1" refY="2" orient="auto"><path d="M0,0 L4,2 L0,4 Z" fill="var(--red)"/></marker>
      <linearGradient id="photo-dark" x1="0" y1="0" x2="0" y2="1"><stop offset="0" stop-color="#2a2a2a"/><stop offset="1" stop-color="#0b0b0b"/></linearGradient>
      <linearGradient id="photo-tray" x1="0" y1="0" x2="1" y2="1"><stop offset="0" stop-color="#3a4d66"/><stop offset="1" stop-color="#1b2838"/></linearGradient>
      <linearGradient id="photo-light" x1="0" y1="0" x2="1" y2="1"><stop offset="0" stop-color="#1a2230"/><stop offset="1" stop-color="#7fbdb0"/></linearGradient>
      <linearGradient id="photo-mouth" x1="0" y1="0" x2="0" y2="1"><stop offset="0" stop-color="#b04a5e"/><stop offset="1" stop-color="#7d2a3a"/></linearGradient>
      <linearGradient id="photo-gum" x1="0" y1="0" x2="0" y2="1"><stop offset="0" stop-color="#e8c7c4"/><stop offset="1" stop-color="#b8283e"/></linearGradient>
      <linearGradient id="figure-fill" x1="0" y1="0" x2="0" y2="1"><stop offset="0" stop-color="#dfe7ee"/><stop offset="1" stop-color="#3d6a8e"/></linearGradient>
    </defs>

    <g class="connectors" stroke-width="30" stroke-linecap="round">
      <line x1="374" y1="639" x2="374" y2="392" stroke="var(--green)"/>
      <line x1="374" y1="639" x2="606" y2="577" stroke="var(--navy)"/>
      <line x1="374" y1="639" x2="510" y2="842" stroke="var(--blue)"/>
      <line x1="374" y1="639" x2="237" y2="842" stroke="var(--red)"/>
      <line x1="374" y1="639" x2="142" y2="586" stroke="var(--teal)"/>
      <line x1="360" y1="668" x2="230" y2="640" stroke="var(--orange)" stroke-width="20"/>
    </g>

    <g class="flow-arrows" fill="none" stroke-width="16">
      <path d="M445,385 Q540,395 565,455" stroke="var(--yellow)" marker-end="url(#head-yellow)"/>
      <path d="M640,665 Q635,720 605,755" stroke="var(--navy)" marker-end="url(#head-navy)"/>
      <path d="M425,858 L340,858" stroke="var(--blue)" marker-end="url(#head-blue)"/>
      <path d="M185,765 L160,690" stroke="var(--red)" marker-end="url(#head-red)"/>
    </g>

    <g class="step step-01" transform="translate(374,392)">
      <use href="#hex-frame" fill="var(--green)" stroke="var(--green)" stroke-width="10" stroke-linejoin="round"/>
      <use href="#hex-photo" fill="url(#photo-dark)" role="img" aria-label="Photo of a handpiece with abutment on a black background"/>
    </g>
    <g class="step step-02" transform="translate(606,577)">
      <use href="#hex-frame" fill="var(--navy)" stroke="var(--navy)" stroke-width="10" stroke-linejoin="round"/>
      <use href="#hex-photo" fill="url(#photo-tray)" role="img" aria-label="Photo of a silicone mould tray with abutment"/>
    </g>
    <g class="step step-03" transform="translate(510,842)">
      <use href="#hex-frame" fill="var(--blue)" stroke="var(--blue)" stroke-width="10" stroke-linejoin="round"/>
      <use href="#hex-photo" fill="url(#photo-light)" role="img" aria-label="Photo of curing light in a gloved hand"/>
    </g>
    <g class="step step-04" transform="translate(237,842)">
      <use href="#hex-frame" fill="var(--red)" stroke="var(--red)" stroke-width="10" stroke-linejoin="round"/>
      <use href="#hex-photo" fill="url(#photo-mouth)" role="img" aria-label="Photo of healing abutment placed in the mouth"/>
    </g>
    <g class="step step-05" transform="translate(142,586)">
      <use href="#hex-frame" fill="var(--teal)" stroke="var(--teal)" stroke-width="10" stroke-linejoin="round"/>
      <use href="#hex-photo" fill="url(#photo-gum)" role="img" aria-label="Photo of healed gum contour around implant"/>
    </g>

    <g class="hub" transform="translate(374,639)">
      <circle r="90" fill="var(--ring)"/>
      <circle r="80" fill="var(--white)"/>
      <circle r="73" fill="url(#figure-fill)" role="img" aria-label="Illustration of a dentist in a white coat"/>
    </g>

    <text class="step-no" x="369" y="282" fill="var(--green)">01</text>
    <text class="step-no" x="612" y="463" fill="var(--orange)">02</text>
    <text class="step-no" x="510" y="990" fill="var(--red)">03</text>
    <text class="step-no" x="229" y="990" fill="var(--maroon)">04</text>
    <text class="step-no" x="142" y="458" fill="var(--maroon)">05</text>
  </svg>

  <footer class="offer-band">
    <p class="offer-kicker">AVAILABLE IN</p>
    <p class="offer-main">SILICONE AND 3D PRINTED</p>
  </footer>
</main>
</body>
</html>
```